Residential Fence Company needs a Flyer Design

We need a flyer design for a fence company called "Brovalent". We custom build Wood, Vinyl, and Aluminum fences for residential customers. The flyer will be a sales promotion offering $500 off for a new fence installation. Prospective customers can call for a FREE estimate

We would like to showcase pictures of the fences we install (attached). We would like to see color designs/themes that that compliment our logo (attached). Additional information to include:

Website: www.brovalentgates.example
Phone Number: (317) 555-0148
Address: 2813 W. Maplewick Ave. Indianapolis, IN 46299

```html
<!DOCTYPE html>
<html lang="en">
<head>
<meta charset="utf-8">
<title>Brovalent – $500 Off Fence Installation Flyer</title>
<link rel="stylesheet" href="https://fonts.googleapis.com/css2?family=Barlow+Condensed:wght@400;500;600&family=Cinzel:wght@700&display=swap">
<style>
  :root {
    --backdrop: #e9e9e9;
    --paper: #ffffff;
    --navy: #1e2a4e;
    --slate-blue: #3e4b74;
    --wine-overlay: rgba(105, 12, 24, 0.72);
    --white: #ffffff;
    --logo-navy: #26376b;
  }
  * { box-sizing: border-box; margin: 0; padding: 0; }
  html, body { width: 1200px; height: 1200px; overflow: hidden; background: var(--backdrop); }
  body { font-family: "Barlow Condensed", "Arial Narrow", sans-serif; }

  .flyer {
    position: absolute; left: 219px; top: 60px;
    width: 762px; height: 1080px;
    background: var(--paper); overflow: hidden;
  }
  .hero-photo {
    position: absolute; left: 0; top: 0; width: 762px; height: 571px;
    background:
      linear-gradient(90deg, rgba(10,14,12,0.15) 0%, rgba(10,14,12,0.55) 60%, rgba(10,14,12,0.25) 100%),
      linear-gradient(180deg, #6f8c5a 0%, #3c5633 35%, #25331f 70%, #1b2419 100%);
  }
  .brand-box {
    position: absolute; left: 52px; top: 61px; width: 289px; height: 141px;
    background: var(--white);
    display: flex; align-items: center; justify-content: center; gap: 12px;
  }
  .brand-mark { width: 18px; height: 18px; background: var(--logo-navy); }
  .brand-name {
    font-family: "Barlow Condensed", sans-serif; font-weight: 600;
    font-size: 46px; letter-spacing: 2px; color: var(--logo-navy); text-transform: uppercase;
  }

  .offer-panel {
    position: absolute; left: 398px; top: 310px; width: 335px; height: 261px;
    background: var(--wine-overlay); color: var(--white); text-align: center;
  }
  .offer-amount {
    position: absolute; left: 0; right: 0; top: 52px;
    font-size: 118px; font-weight: 500; line-height: 1; letter-spacing: -1px;
  }
  .offer-amount .offer-suffix { font-size: 40px; font-weight: 400; letter-spacing: 1px; margin-left: 2px; }
  .offer-terms {
    position: absolute; left: 0; right: 0; top: 183px;
    font-size: 27px; font-weight: 400; text-transform: uppercase; letter-spacing: 0.3px;
  }
  .offer-terms strong, .estimate-panel strong { font-weight: 600; }

  .estimate-panel {
    position: absolute; left: 399px; top: 574px; width: 335px; height: 141px;
    background: var(--slate-blue); color: var(--white);
    display: flex; flex-direction: column; align-items: center; justify-content: center;
    font-size: 28px; line-height: 1.3; text-transform: uppercase; text-align: center;
  }

  .fence-photo { position: absolute; }
  .fence-photo--vinyl {
    left: 52px; top: 467px; width: 324px; height: 162px;
    background: linear-gradient(180deg, #5d97d8 0%, #cfe2f2 38%, #f2f4f5 52%, #c9ced2 62%, #5a8f2e 72%, #3f7122 100%);
  }
  .fence-photo--aluminum {
    left: 52px; top: 659px; width: 324px; height: 216px;
    background: linear-gradient(180deg, #6c9fd6 0%, #c5d9ea 40%, #5f6e5a 62%, #6f9a3c 82%, #4f7d26 100%);
  }
  .fence-photo--wood {
    left: 399px; top: 741px; width: 335px; height: 223px; z-index: 2;
    background: linear-gradient(180deg, #8a9a92 0%, #4b5e3e 25%, #e3cfa6 45%, #d8bf91 68%, #3f6a2a 85%, #335a22 100%);
  }

  .contact-band {
    position: absolute; left: 0; top: 906px; width: 762px; height: 139px;
    background: var(--navy); color: var(--white);
  }
  .contact-list { list-style: none; position: absolute; left: 52px; top: 30px; }
  .contact-item {
    display: flex; align-items: center; gap: 14px;
    font-size: 22px; line-height: 28px; text-transform: uppercase; letter-spacing: 0.3px;
  }
  .contact-icon { width: 14px; height: 14px; flex: none; fill: var(--white); }
</style>
</head>
<body>
  <main class="flyer">
    <div class="hero-photo" role="img" aria-label="Close-up photo of a black aluminum fence with post cap against blurred green garden"></div>

    <div class="brand-box">
      <span class="brand-mark"></span>
      <span class="brand-name">Brovalent</span>
    </div>

    <section class="offer-panel">
      <p class="offer-amount">$500<span class="offer-suffix">OFF</span></p>
      <p class="offer-terms">For a new fence <strong>installation</strong></p>
    </section>

    <section class="estimate-panel">
      <p>Prospective customers can</p>
      <p>call for a <strong>free estimate</strong></p>
    </section>

    <div class="fence-photo fence-photo--vinyl" role="img" aria-label="White vinyl privacy fence along a green lawn under blue sky"></div>
    <div class="fence-photo fence-photo--aluminum" role="img" aria-label="Black aluminum fence running across a grassy yard"></div>
    <div class="fence-photo fence-photo--wood" role="img" aria-label="Natural wood picket fence beside a lawn"></div>

    <footer class="contact-band">
      <ul class="contact-list">
        <li class="contact-item">
          <svg class="contact-icon" viewBox="0 0 14 14" aria-hidden="true"><rect x="3" y="0" width="8" height="14" rx="1.5"/><rect x="4.5" y="2" width="5" height="8" fill="#1e2a4e"/></svg>
          (317) 555-0148
        </li>
        <li class="contact-item">
          <svg class="contact-icon" viewBox="0 0 14 14" aria-hidden="true"><rect x="0" y="2" width="14" height="10" rx="1"/><path d="M0.8 3 L7 8 L13.2 3" fill="none" stroke="#1e2a4e" stroke-width="1.3"/></svg>
          www.brovalentgates.example
        </li>
        <li class="contact-item">
          <svg class="contact-icon" viewBox="0 0 14 14" aria-hidden="true"><circle cx="7" cy="7" r="7"/><circle cx="7" cy="5.5" r="2" fill="#1e2a4e"/><path d="M7 12 L4.6 6.6 H9.4 Z" fill="#1e2a4e"/></svg>
          2813 W. Maplewick Ave. Indianapolis, IN 46299
        </li>
      </ul>
    </footer>
  </main>
</body>
</html>
```